Wordpress Design for Software Company

I have a website that is not developed in WordPress. I need the current site www.brenwix.com/projects/tormelink to be redesigned in Wordpress. I would to keep some of the look and feel but change other things.
1) such as logo background color
2) have (3) columns in on inner pages
3) so nice pictures or graphic layouts I am hoping that you will be able to improve on the look of the website.
Target Market(s)
B2B Companies that deploy call centers or have inside sales staff.
Industry/Entity Type
It Company
Look and feel

```html
<!DOCTYPE html>
<html lang="en">
<head>
<meta charset="utf-8">
<title>TormeLink – Call Center Solutions</title>
<link rel="stylesheet" href="https://fonts.googleapis.com/css2?family=Arimo:wght@400;700&family=Lora:ital,wght@0,700;1,400;1,700&family=Oswald:wght@600&family=Roboto+Condensed:wght@700&family=Varela+Round&display=swap">
<style>
:root{
  --sky-top:#0f8fe0;
  --sky-bottom:#1a72d6;
  --page:#ffffff;
  --frame:#dcdcdc;
  --nav-top:#36b3f0;
  --nav-bottom:#0a86d2;
  --nav-line:#0667a8;
  --orange-top:#ffb42a;
  --orange-bottom:#f58a00;
  --orange-text:#f39a14;
  --sand:#e7e3cf;
  --panel-grey:#e6e9ec;
  --blue-box-top:#1a9fd8;
  --blue-box-bottom:#0b6fae;
  --footer:#4a4f55;
  --footer-rule:#5f646a;
  --ink:#222;
  --white:#fff;
}
*{box-sizing:border-box;margin:0;padding:0}
html,body{width:1030px;height:1200px;overflow:hidden}
body{
  position:relative;
  background:linear-gradient(180deg,var(--sky-top),var(--sky-bottom));
  font-family:"Arimo",Arial,sans-serif;color:var(--ink);
}
.abs{position:absolute}
.page{left:72px;top:16px;width:883px;height:1144px;background:var(--page);}
.header{left:76px;top:18px;width:875px;height:137px;
  background:linear-gradient(160deg,#cfeaf6 0%,#f6fbfd 35%,#ffffff 55%,#bfe2f3 100%);}
.brand{left:118px;top:62px;display:flex;align-items:center;gap:12px;
  font-family:"Arimo",Arial,sans-serif;font-size:30px;color:#1d5f9e;font-weight:400}
.brand-mark{width:40px;height:40px;border-radius:50%;background:#f28c0f}
.account{left:783px;top:122px;width:155px;height:32px;border-radius:5px 5px 0 0;
  background:linear-gradient(var(--orange-top),var(--orange-bottom));
  color:var(--white);font-family:"Varela Round",sans-serif;font-size:15px;
  display:flex;align-items:center;justify-content:center;gap:10px}
.ribbon{top:172px;height:40px;width:60px}
.nav{left:60px;top:158px;width:906px;height:42px;display:flex;
  background:linear-gradient(var(--nav-top),var(--nav-bottom));border-radius:3px}
.nav a{display:flex;align-items:center;justify-content:center;color:#04243d;
  text-decoration:none;font-family:"Varela Round",sans-serif;font-size:16px;
  border-right:1px solid var(--nav-line)}
.nav a:last-child{border-right:none}
.nav a.current{color:var(--white)}
.box{border:1px solid var(--frame);background:var(--white);padding:5px}
.sidebar{left:87px;top:213px;width:277px;height:277px}
.sidebar-inner{width:100%;height:100%;background:var(--sand);position:relative;padding:14px 10px}
.search{display:flex;gap:6px}
.search-field{width:180px;height:21px;background:var(--white);border:1px solid #bbb}
.btn{background:linear-gradient(var(--orange-top),var(--orange-bottom));color:var(--white);
  font-size:13px;font-weight:700;display:flex;align-items:center;justify-content:center;border-radius:2px}
.search .btn{width:72px;height:21px}
.news-title{font-family:"Lora",serif;font-style:italic;font-weight:700;font-size:19px;
  color:#3a3a3a;margin:16px 0 10px 4px;border-top:1px solid #cfcab3;padding-top:10px}
.news p{font-size:11px;line-height:13px;margin:0 0 13px 8px;color:#222}
.learn{position:absolute;right:10px;bottom:12px;width:94px;height:22px}
.hero{left:381px;top:213px;width:560px;height:280px}
.hero-photo{width:100%;height:100%;position:relative;
  background:linear-gradient(90deg,#3a4a5e 0%,#8a7d6c 30%,#cfc6b0 60%,#e5e1cf 100%)}
.hero-line{position:absolute;left:236px;top:100px;font-family:"Oswald",sans-serif;font-weight:600;
  font-size:25px;color:var(--orange-text);letter-spacing:-.3px}
.about{left:87px;top:507px;width:623px;height:360px}
.about-inner{background:var(--panel-grey);width:100%;height:100%;position:relative;padding:0 8px}
.tabs{display:flex;gap:3px;height:42px;margin-top:5px;background:linear-gradient(var(--orange-top),var(--orange-bottom));padding:5px 80px 0 4px}
.tab{flex:1;border-radius:6px 6px 0 0;font-family:"Lora",serif;font-style:italic;font-size:15px;
  color:var(--white);display:flex;align-items:center;justify-content:center;
  background:linear-gradient(#2f88c4,#0d5b96)}
.tab.active{background:var(--panel-grey);color:#111}
.team-photo{position:absolute;left:8px;top:59px;width:185px;height:140px;
  background:linear-gradient(180deg,#e9ebec,#b9b6b0 60%,#8b8a88)}
.about-title{position:absolute;left:207px;top:63px;font-family:"Lora",serif;font-style:italic;
  font-weight:700;font-size:16px;color:var(--orange-text)}
.about-lead{position:absolute;left:205px;top:90px;width:403px;font-size:12px;line-height:17px}
.about-more{position:absolute;left:8px;top:243px;width:600px;font-size:12px;line-height:18px}
.blue-box{background:linear-gradient(var(--blue-box-top),var(--blue-box-bottom));width:100%;height:100%;padding:16px 10px;color:var(--white)}
.links{left:721px;top:506px;width:221px;height:164px}
.contact{left:721px;top:683px;width:221px;height:184px}
.blue-box h3{font-family:"Roboto Condensed",sans-serif;font-size:17px;color:#061a2a;margin-bottom:8px}
.contact h3{color:#061a2a}
.links ul{list-style:none;font-size:11.5px;font-weight:700}
.links li{margin:0 0 12px 8px}
.links li::before,.footer li::before{content:"» ";}
.phone-row{display:flex;align-items:flex-start;gap:6px;margin-top:10px}
.phone-num{font-size:23px;line-height:22px}
.phone-num small{display:block;font-size:13px}
.mail-row{display:flex;align-items:center;gap:8px;font-size:12px;margin-top:12px}
.follow{display:flex;align-items:center;gap:10px;margin-top:12px;font-size:17px}
.social{width:38px;height:38px;border-radius:5px;background:#2aa4d8;border:2px solid #dff2fb}
.social.alt{background:#3b5e9c}
.footer{left:87px;top:883px;width:851px;height:260px;background:var(--footer);color:var(--white);padding:18px 20px}
.footer .col{position:absolute;top:18px}
.footer h4{font-family:"Lora",serif;font-weight:700;font-size:14px;margin-bottom:10px}
.footer ul{list-style:none;font-size:11px;line-height:14px}
.footer li{margin-bottom:10px;padding-left:8px}
.rule{position:absolute;top:55px;width:1px;height:155px;background:var(--footer-rule)}
.copy{position:absolute;right:25px;bottom:14px;font-size:11px}
</style>
</head>
<body>
<div class="abs page"></div>

<header>
  <div class="abs header" role="img" aria-label="Soft sky with white clouds"></div>
  <div class="abs brand"><span class="brand-mark"></span>TormeLink</div>
  <div class="abs account"><span>Log in</span><span>|</span><span>Register</span></div>
  <svg class="abs ribbon" style="left:14px" viewBox="0 0 60 40"><polygon points="0,10 60,0 60,38 8,28 18,20" fill="#1c8ad6"/></svg>
  <svg class="abs ribbon" style="left:956px" viewBox="0 0 60 40"><polygon points="0,0 60,10 42,20 52,28 0,38" fill="#1c8ad6"/></svg>
  <nav class="abs nav">
    <a class="current" href="#" style="width:121px">Home</a>
    <a href="#" style="width:159px">Products</a>
    <a href="#" style="width:162px">Soultions</a>
    <a href="#" style="width:167px">Resources</a>
    <a href="#" style="width:155px">Services</a>
    <a href="#" style="width:142px">Contacts</a>
  </nav>
</header>

<aside class="abs box sidebar">
  <div class="sidebar-inner">
    <div class="search"><div class="search-field"></div><div class="btn">Search</div></div>
    <h2 class="news-title">What's New</h2>
    <div class="news">
      <p>Remote IP Agent/Virtual Agent</p>
      <p>TormeLink and Varnhold Channel Network Partner Silverline Net Communication Provide a "Universal Phone" Solution to NY based Mortgage Finance Company</p>
      <p>Find out what people are saying about the TormeLink Hosted Predictive Dialer System</p>
    </div>
    <div class="btn learn">Learn More</div>
  </div>
</aside>

<section class="abs box hero">
  <div class="hero-photo" role="img" aria-label="Smiling call center agent wearing a headset in an office">
    <div class="hero-line">Lorem Ipsum dolor sit amet</div>
  </div>
</section>

<section class="abs box about">
  <div class="about-inner">
    <div class="tabs">
      <div class="tab active">Who we are</div>
      <div class="tab">What we do</div>
      <div class="tab">Our Clients</div>
      <div class="tab">Try &nbsp;us out</div>
    </div>
    <div class="team-photo" role="img" aria-label="Group portrait of the business team"></div>
    <h3 class="about-title">Who we are</h3>
    <p class="about-lead">Practical call center solutions for the contact center industry<br>TormeLink is an industry-leader in the development of call center solutions and predictive dialers for industry-specific applications ranging from financial services to home remodeling and other related companies that utilize the services of Predictive Dialing and Contact Center Management &amp; Customer Interaction. We offer both premise based and hosted solutions to small to medium-sized inside sales organizations to larger call centers.</p>
    <p class="about-more">Our goal is to provide a seamless cost effective call center solutions which involves the cohesive blend of computer telephony integration (CTI) applications, web centric applications, customer relationship (CRM), agent interaction and other channels of communications such as web call back, web chat, email, fax and web collaboration</p>
  </div>
</section>

<aside class="abs box links">
  <div class="blue-box">
    <h3>Important links</h3>
    <ul>
      <li>Products</li>
      <li>Hosted Applications</li>
      <li>Integrated Dialing Solutions</li>
      <li>Industry Specific Solutions</li>
    </ul>
  </div>
</aside>

<aside class="abs box contact">
  <div class="blue-box">
    <h3>Contact Us</h3>
    <div class="phone-row">
      <svg width="24" height="30" viewBox="0 0 24 30"><path d="M5 2c2 0 4 5 3 7l-2 2c1 4 4 8 7 10l2-2c2-1 7 1 7 3l-3 4c-9 0-18-12-17-21z" fill="#e2261c"/></svg>
      <div class="phone-num">1.888.555.0142<small>(Toll FREE)</small></div>
    </div>
    <div class="mail-row">
      <svg width="26" height="17" viewBox="0 0 26 17"><rect width="26" height="17" rx="2" fill="#f5c233"/><path d="M1 1l12 9 12-9" stroke="#c98a10" stroke-width="1.5" fill="none"/></svg>
      sales@tormelinkcorp.com
    </div>
    <div class="follow">Follow us <span class="social"></span><span class="social alt"></span></div>
  </div>
</aside>

<footer class="abs footer">
  <div class="col" style="left:20px">
    <h4>Products</h4>
    <ul>
      <li>Hosted Predictive Dialer</li>
      <li>Inbound/Outbound Blended Dialer &amp; ACD</li>
      <li>CallStation™ Premise Based Predictive<br>Dialer</li>
      <li>Contact Manager CRM</li>
      <li>Auto, Preview and Progressive Dialing</li>
      <li>IVR/Power Voice</li>
      <li>Digital Call Recording</li>
    </ul>
  </div>
  <div class="rule" style="left:272px"></div>
  <div class="col" style="left:311px">
    <h4>Solutions</h4>
    <ul>
      <li>Hosted Solutions</li><li>Premise Based</li><li>Industry Specific</li>
      <li>Small Office</li><li>Mid Size</li><li>Enterprise</li>
    </ul>
  </div>
  <div class="rule" style="left:454px"></div>
  <div class="col" style="left:491px">
    <h4>Resources</h4>
    <ul><li>Applications</li><li>Resources Link 2</li></ul>
  </div>
  <div class="rule" style="left:628px"></div>
  <div class="col" style="left:664px">
    <h4>Services</h4>
    <ul><li>Technical Support</li><li>Consulting &amp; Programming</li><li>Telecom Services - PBX</li></ul>
  </div>
  <div class="copy">© 2011 tormelinkcorp.com. All Rights Reserved.</div>
</footer>
</body>
</html>
```